business card design for a plumbing contractor

i need a double business card for a plumbing business, our initial service is residential Sewer Drain Cleaning.

Target Market(s)

other plumbing Business

Industry/Entity Type

Plumbing

Contact Information for Business Card

www.PipeworksTopNotch.example- 5173829046-

Font styles to use
Serif

Colors
ec1f27
0455a3

```html
<!DOCTYPE html>
<html lang="en">
<head>
<meta charset="utf-8">
<title>Pipeworks TopNotch — Business Card</title>
<link href="https://fonts.googleapis.com/css2?family=Poppins:wght@400;500;600&display=swap" rel="stylesheet">
<style>
  :root {
    --brand-blue: #0455a3;
    --brand-red: #ec1f27;
    --card-white: #f4f3f3;
    --ink: #222222;
    --logo-taupe: #8a7f72;
    --backdrop: #0d0d0d;
  }
  * { margin: 0; padding: 0; box-sizing: border-box; }
  html, body { width: 1200px; height: 916px; overflow: hidden; }
  body {
    background: radial-gradient(ellipse at 60% 35%, #262626 0%, var(--backdrop) 70%);
    font-family: "Poppins", sans-serif;
    position: relative;
  }
  .card { position: absolute; width: 676px; height: 385px; border-radius: 34px; overflow: hidden; }

  /* Front */
  .card-front { left: 86px; top: 34px; background: var(--brand-blue); }
  .front-name {
    position: absolute; left: 0; right: 0; top: 150px;
    text-align: center; color: #ffffff;
    font-weight: 600; font-size: 42px; line-height: 46px; letter-spacing: 0.5px;
  }
  .service-band {
    position: absolute; left: 22px; width: 630px; top: 326px; height: 70px;
    background: var(--brand-red); border-radius: 40px 40px 0 0;
    color: #ffffff; font-size: 18px; display: flex; align-items: flex-start;
    padding: 16px 0 0 25px; white-space: nowrap;
  }
  .service-band .sep { margin: 0 18px; }

  /* Back */
  .card-back { left: 424px; top: 441px; background: var(--card-white); }
  .back-name {
    position: absolute; right: 38px; top: 46px; text-align: right;
    color: var(--logo-taupe); font-weight: 600; font-size: 28px; line-height: 30px;
  }
  .person-name {
    position: absolute; left: 23px; top: 208px;
    color: var(--brand-blue); font-size: 27px; font-weight: 500; letter-spacing: 0.5px;
  }
  .name-rule { position: absolute; left: 23px; right: 23px; top: 246px; height: 2px; background: var(--brand-red); }
  .contact { position: absolute; left: 30px; font-size: 16.5px; color: var(--ink); display: flex; align-items: center; gap: 14px; }
  .contact svg { width: 18px; height: 18px; fill: var(--ink); }
  .contact-phone { top: 262px; }
  .contact-email { top: 292px; }
  .address { position: absolute; left: 500px; top: 262px; font-size: 16.5px; line-height: 19px; color: var(--ink); }
  .footer-bands { position: absolute; left: 0; bottom: 0; width: 676px; height: 52px; }
  .website { position: absolute; right: 29px; bottom: 20px; color: #ffffff; font-size: 16.5px; }
</style>
</head>
<body>
  <section class="card card-front">
    <div class="front-name">Pipeworks<br>TopNotch</div>
    <div class="service-band">
      <span>Sewer Drain Cleaning</span><span class="sep">|</span><span>Maintenance</span><span class="sep">|</span><span>Trenchless Pipe Installs.</span>
    </div>
  </section>

  <section class="card card-back">
    <div class="back-name">Pipeworks<br>TopNotch</div>
    <div class="person-name">DALE MORROW</div>
    <div class="name-rule"></div>
    <div class="contact contact-phone">
      <svg viewBox="0 0 24 24" aria-hidden="true"><path d="M6.6 10.8a15.2 15.2 0 0 0 6.6 6.6l2.2-2.2c.3-.3.7-.4 1-.2 1.1.4 2.3.6 3.6.6.6 0 1 .4 1 1V20c0 .6-.4 1-1 1A17 17 0 0 1 3 4c0-.6.4-1 1-1h3.5c.6 0 1 .4 1 1 0 1.3.2 2.5.6 3.6.1.3 0 .7-.2 1z"/></svg>
      <span>5173829046</span>
    </div>
    <div class="contact contact-email">
      <svg viewBox="0 0 24 24" aria-hidden="true"><path d="M2 5h20v2l-10 6L2 7z"/><path d="M2 9l10 6 10-6v10H2z"/></svg>
      <span>Dispatch@PipeworksTopNotch.example</span>
    </div>
    <div class="address">Your address, City,<br>State, Zip</div>
    <svg class="footer-bands" viewBox="0 0 676 52" aria-hidden="true">
      <polygon points="0,30 304,30 288,52 0,52" fill="var(--brand-red)"/>
      <path d="M308,52 C330,30 345,0 380,0 L676,0 L676,52 Z" fill="var(--brand-blue)"/>
    </svg>
    <div class="website">www.PipeworksTopNotch.example</div>
  </section>
</body>
</html>
```